Rack card for a integrative medical practice

Need an eye-catching rack card with our logo with content as provided. We have a membership based holistic medical practice which incorporates western and holistic medicine. We would like to focus on wellness and healthy lifestyle. See uploaded files for what is included in the membership. Would like 2 page rack card color on both sides. Logo must be on the front.

Target Market(s)

People looking for alternative medicine, healthy lifestyle.

Industry/Entity Type

Health and Wellness

Colors
00AB8E
00BBA5
67D7C9
C6EFE9
E9F9F6

Requirements
Must have
• Must spark interest at first sight. Clear message.
Nice to have
• Warm, bright and positive vibe. Organic, neutral and earthy colors.
Should not have
• Traditional medical practice vibe (cold, formal, industrial). No PINK except the logo.

```html
<!DOCTYPE html>
<html lang="en">
<head>
<meta charset="utf-8">
<title>Willowmere Health &amp; Wellness – Rack Card</title>
<link rel="stylesheet" href="https://fonts.googleapis.com/css2?family=Comfortaa:wght@400&family=Tinos:wght@400&family=Arimo:wght@400&display=swap">
<style>
  :root {
    --teal: #3aaea9;
    --teal-text: #3cb2aa;
    --band: #acd4dc;
    --ring: #8ccbe6;
    --ink: #1c1c1c;
    --body: #3b3b3b;
    --rule: #8a8a8a;
    --paper: #ffffff;
    --border: #b9b9b9;
  }
  * { box-sizing: border-box; margin: 0; padding: 0; }
  html, body { width: 1200px; height: 1200px; overflow: hidden; background: var(--paper); }
  .canvas { position: relative; width: 1200px; height: 1200px; background: var(--paper); }

  .card {
    position: absolute; width: 427px; height: 962px;
    background: var(--paper); border: 1px solid var(--border); overflow: hidden;
  }
  .card--front { left: 127px; top: 121px; }
  .card--back  { left: 646px; top: 117px; }

  .card__art { position: absolute; left: 0; top: 0; width: 427px; height: 560px; }

  .footer-band { position: absolute; left: 0; top: 873px; width: 100%; height: 89px; background: var(--band); }

  /* front */
  .brand-badge {
    position: absolute; left: 28px; top: 402px; width: 150px; height: 150px;
    border-radius: 50%; border: 1px solid var(--ring); background: transparent;
  }
  .brand-badge__inner {
    position: absolute; left: 6px; top: 6px; width: 136px; height: 136px; border-radius: 50%;
    background: var(--paper); display: flex; flex-direction: column; align-items: center; justify-content: center;
  }
  .brand-name {
    font-family: "Tinos", serif; font-weight: 400; color: var(--ink); font-size: 15px; letter-spacing: 1px;
    text-align: center; line-height: 1.15;
  }
  .tagline { position: absolute; left: 0; width: 100%; text-align: center; font-family: "Comfortaa", sans-serif; font-weight: 400; white-space: nowrap; }
  .tagline--lead   { top: 610px; font-size: 29px; color: var(--teal-text); }
  .tagline--plain  { top: 670px; font-size: 22px; color: var(--ink); }
  .tagline--accent { top: 724px; font-size: 24px; color: var(--teal-text); }
  .tagline--close  { top: 775px; font-size: 22px; color: var(--ink); }
  .address {
    position: absolute; left: 0; top: 893px; width: 100%; text-align: center;
    font-family: "Arimo", sans-serif; font-size: 17px; line-height: 25px; color: var(--ink);
  }

  /* back */
  .benefits-heading { position: absolute; left: 74px; top: 236px; font-family: "Tinos", serif; font-weight: 400; }
  .benefits-heading__kicker { display: block; font-size: 24px; color: var(--ink); }
  .benefits-heading__title { display: block; font-size: 54px; color: var(--teal-text); line-height: 1.05; margin-top: 2px; }
  .timeline { position: absolute; left: 0; top: 0; width: 427px; height: 800px; }
  .benefit {
    position: absolute; left: 73px; width: 345px;
    font-family: "Arimo", sans-serif; font-size: 16.3px; line-height: 24px; color: var(--body);
  }
  .benefit--narrow { width: 290px; }
  .photo-ring {
    position: absolute; top: 796px; width: 144px; height: 144px; border-radius: 50%;
    border: 1.5px solid var(--ring); background: var(--paper);
  }
  .photo-ring__fill { position: absolute; left: 7px; top: 7px; width: 128px; height: 128px; border-radius: 50%; }
  .photo-ring--treatment { left: 51px; }
  .photo-ring--treatment .photo-ring__fill { background: radial-gradient(circle at 60% 45%, #e9c9b3, #c79a80 55%, #f3eee9 90%); }
  .photo-ring--spa { left: 233px; }
  .photo-ring--spa .photo-ring__fill { background: radial-gradient(circle at 40% 60%, #3a3a38, #5f8a3a 55%, #e8ede6 90%); }
</style>
</head>
<body>
<div class="canvas">

  <section class="card card--front">
    <svg class="card__art" viewBox="0 0 427 560" role="img" aria-label="Photo of a person meditating cross-legged on a teal yoga mat with prayer beads">
      <defs>
        <linearGradient id="yogaTones" x1="0" y1="0" x2="1" y2="1">
          <stop offset="0" stop-color="#c9dc4a"/>
          <stop offset="0.35" stop-color="#b9c85a"/>
          <stop offset="0.6" stop-color="#2f6e85"/>
          <stop offset="1" stop-color="#7f8a8c"/>
        </linearGradient>
        <clipPath id="frontClip"><path d="M0 0 H427 V500 C330 560 230 540 160 510 L0 394 Z"/></clipPath>
      </defs>
      <rect width="427" height="560" fill="url(#yogaTones)" clip-path="url(#frontClip)"/>
      <path d="M0 394 C40 420 60 432 80 438 L0 430 Z" fill="var(--teal)"/>
      <path d="M150 508 C230 545 330 565 427 500 C340 545 240 548 150 512 Z" fill="var(--teal)"/>
    </svg>
    <div class="brand-badge">
      <div class="brand-badge__inner">
        <span class="brand-name">WILLOWMERE<br>HEALTH &amp; WELLNESS</span>
      </div>
    </div>
    <p class="tagline tagline--lead">A direct primary Care</p>
    <p class="tagline tagline--plain">Practice focused on a more</p>
    <p class="tagline tagline--accent">Holistic &amp; Personal Approach</p>
    <p class="tagline tagline--close">to Medicine</p>
    <div class="footer-band"></div>
    <p class="address">1247 Oak Ridge Ave., STE 2B<br>Brookhaven</p>
  </section>

  <section class="card card--back">
    <svg class="card__art" viewBox="0 0 427 560" role="img" aria-label="Photo of a sunlit green meadow with soft light rays">
      <defs>
        <linearGradient id="meadowTones" x1="0" y1="0" x2="0" y2="1">
          <stop offset="0" stop-color="#dfe8ee"/>
          <stop offset="0.35" stop-color="#8fbf5a"/>
          <stop offset="1" stop-color="#a9d43a"/>
        </linearGradient>
        <clipPath id="backClip"><path d="M0 0 H427 V194 C380 225 320 232 280 228 C180 222 90 160 0 82 Z"/></clipPath>
      </defs>
      <rect width="427" height="240" fill="url(#meadowTones)" clip-path="url(#backClip)"/>
      <path d="M0 82 C90 160 180 222 280 228 C320 232 380 225 427 194 C380 232 320 240 280 236 C170 230 80 175 0 100 Z" fill="var(--teal)"/>
    </svg>

    <h2 class="benefits-heading">
      <span class="benefits-heading__kicker">What's Included In Your</span>
      <span class="benefits-heading__title">Membership</span>
    </h2>

    <svg class="timeline" viewBox="0 0 427 800" aria-hidden="true">
      <path d="M66 255 H41 Q37 255 37 259 V756" fill="none" stroke="var(--rule)" stroke-width="1.3"/>
      <g fill="var(--paper)" stroke="var(--rule)" stroke-width="1.3">
        <circle cx="37" cy="373" r="7.5"/>
        <circle cx="37" cy="416" r="7.5"/>
        <circle cx="37" cy="458" r="7.5"/>
        <circle cx="37" cy="502" r="7.5"/>
        <circle cx="37" cy="546" r="7.5"/>
        <circle cx="37" cy="589" r="7.5"/>
        <circle cx="37" cy="656" r="7.5"/>
        <circle cx="37" cy="699" r="7.5"/>
      </g>
    </svg>

    <p class="benefit" style="top:361px">Unlimited office visits with no copay</p>
    <p class="benefit" style="top:404px">Direct communication with your doctor</p>
    <p class="benefit" style="top:446px">Discounted labs, imaging and medications</p>
    <p class="benefit" style="top:490px">Free initial acupuncture session ($250 value)</p>
    <p class="benefit" style="top:534px">2 Vitalyze testings per year ($100 value)</p>
    <p class="benefit benefit--narrow" style="top:577px">Discounts for supplements and health products in the clinic</p>
    <p class="benefit" style="top:644px">Discounts for iv vitamin infusion therapy</p>
    <p class="benefit" style="top:687px">Personalized nutrition plan after&nbsp; advanced testing such as gut microbiome, hormonal, metabolism test, etc</p>

    <div class="footer-band"></div>
    <div class="photo-ring photo-ring--treatment">
      <div class="photo-ring__fill" role="img" aria-label="Photo of an acupuncture treatment on a patient's back"></div>
    </div>
    <div class="photo-ring photo-ring--spa">
      <div class="photo-ring__fill" role="img" aria-label="Photo of spa stones, white orchids and candles"></div>
    </div>
  </section>

</div>
</body>
</html>
```